Delvin & Associates - London New Letting and Property Management Company *

Delvin & Associates LTD is a new company based in London, and works with brand new residential property in the city centre.

We are aiming to have 1000 new properties a year.

We are looking for something modern and minimalistic :
Logo ,Monogram, Paper Head and Business Card.

Target Market(s)

Internation landlords

Industry/Entity Type

Real Estate

Logo Text

Delvin & Associates

Colors

Designer to choose colors to be used in the design.

Requirements
Nice to have
• A particular monogram with "DA"
Should not have
• Little House over the logo

```html
<!DOCTYPE html>
<html lang="en">
<head>
<meta charset="utf-8">
<title>Delvin &amp; Associates LTD – Letterhead</title>
<link rel="stylesheet" href="https://fonts.googleapis.com/css2?family=Lato:wght@400&display=swap">
<style>
  :root {
    --backdrop: #ffffff;
    --paper: #ffffff;
    --header-band: #e6e7e8;
    --ink: #000000;
    --muted: #7d7d7d;
    --monogram-text: #ffffff;
    --shadow: rgba(0, 0, 0, 0.28);
  }
  * { margin: 0; padding: 0; box-sizing: border-box; }
  html, body {
    width: 1200px;
    height: 1000px;
    overflow: hidden;
    background: var(--backdrop);
    font-family: "Lato", sans-serif;
  }
  .letterhead {
    position: absolute;
    left: 302px;
    top: 69px;
    width: 596px;
    height: 863px;
    background: var(--paper);
    box-shadow: 0 12px 50px 6px var(--shadow);
  }
  .letterhead__header {
    position: relative;
    height: 159px;
    background: var(--header-band);
  }
  .monogram {
    position: absolute;
    left: 24px;
    top: 28px;
    width: 65px;
    height: 50px;
    background: var(--ink);
    color: var(--monogram-text);
    font-size: 28px;
    font-weight: 400;
    line-height: 50px;
    text-align: center;
    letter-spacing: 1px;
  }
  .company {
    position: absolute;
    left: 0;
    right: 0;
    top: 68px;
    text-align: center;
  }
  .company__name {
    font-size: 19px;
    font-weight: 400;
    color: var(--ink);
    line-height: 24px;
  }
  .company__tagline {
    margin-top: 4px;
    font-size: 12px;
    color: var(--muted);
    line-height: 15px;
  }
  .header-rule {
    position: absolute;
    left: 107px;
    top: 159px;
    width: 381px;
    height: 4px;
    background: var(--ink);
  }
</style>
</head>
<body>
  <div class="letterhead">
    <header class="letterhead__header">
      <div class="monogram">DA</div>
      <div class="company">
        <p class="company__name">Delvin &amp; Associates LTD</p>
        <p class="company__tagline">Residential Property in The City Centre</p>
      </div>
    </header>
    <div class="header-rule"></div>
  </div>
</body>
</html>
```